Business Card for Brevel Coatings

We need a simple, yet out standing business card for our painting company.

Target Market(s)

wealthy; high-end neighborhoods, and businesses

Industry/Entity Type

Painting

Contact Information for Business Card

Name:
Doran Vask

Email:
d.vask@brevel-coatings.com

Website:
Brevel-coatings.com

Phone Number:
(555) 416-9073

Font styles to use
Serif
Sans Serif

Requirements
Must have
• slogan "making change simple"
Should not have
• A title attached to the name on the card

```html
<!DOCTYPE html>
<html lang="en">
<head>
<meta charset="utf-8">
<title>Brevel Coatings – Business Card</title>
<link href="https://fonts.googleapis.com/css2?family=Cinzel:wght@600&family=PT+Sans:ital,wght@1,400;1,700&display=swap" rel="stylesheet">
<style>
  :root {
    --page: #ffffff;
    --card: #ece9e0;
    --leaf: #a5bd27;
    --forest: #3e5a1d;
    --shadow: rgba(0, 0, 0, 0.38);
  }
  * { margin: 0; padding: 0; box-sizing: border-box; }
  html, body {
    width: 1200px;
    height: 900px;
    overflow: hidden;
    background: var(--page);
  }
  .canvas {
    position: relative;
    width: 1200px;
    height: 900px;
  }
  .card {
    position: absolute;
    left: 346px;
    width: 506px;
    height: 298px;
    background: var(--card);
    box-shadow: 2px 3px 6px var(--shadow);
    overflow: hidden;
  }
  .card--front { top: 77px; }
  .card--back { top: 526px; }

  .wordmark {
    font-family: "Cinzel", serif;
    font-weight: 600;
    color: var(--forest);
    line-height: 1;
  }
  .wordmark__main { display: block; }
  .wordmark__sub { display: block; letter-spacing: 0.32em; }

  .card--front .wordmark {
    position: absolute;
    left: 0;
    right: 0;
    top: 100px;
    text-align: center;
  }
  .card--front .wordmark__main { font-size: 48px; }
  .card--front .wordmark__sub { font-size: 22px; margin-top: 6px; }

  .slogan {
    position: absolute;
    left: 0;
    right: 0;
    top: 192px;
    text-align: center;
    font-family: "PT Sans", sans-serif;
    font-style: italic;
    font-size: 14px;
    letter-spacing: 0.04em;
    color: var(--forest);
  }

  .website {
    position: absolute;
    left: 0;
    right: 0;
    top: 249px;
    text-align: center;
    font-family: "PT Sans", sans-serif;
    font-style: italic;
    font-weight: 700;
    font-size: 14px;
    color: var(--forest);
  }

  .card__swoosh {
    position: absolute;
    inset: 0;
    width: 100%;
    height: 100%;
  }
  .card--back .wordmark {
    position: absolute;
    left: 20px;
    top: 20px;
  }
  .card--back .wordmark__main { font-size: 34px; }
  .card--back .wordmark__sub { font-size: 15px; margin-top: 4px; letter-spacing: 0.28em; }

  .contact {
    position: absolute;
    left: 20px;
    top: 236px;
    list-style: none;
    font-family: "PT Sans", sans-serif;
    font-style: italic;
    font-size: 13.5px;
    color: var(--forest);
  }
  .contact__item {
    display: flex;
    align-items: center;
    gap: 10px;
    height: 21px;
  }
  .contact__icon {
    width: 16px;
    height: 14px;
    flex: none;
    font-style: normal;
    font-weight: 700;
    font-size: 14px;
    text-align: center;
    line-height: 14px;
  }
  .person {
    position: absolute;
    right: 22px;
    top: 238px;
    font-family: "PT Sans", sans-serif;
    font-style: italic;
    font-weight: 700;
    font-size: 28px;
    color: var(--forest);
  }
</style>
</head>
<body>
<main class="canvas">

  <section class="card card--front" aria-label="Card front">
    <p class="wordmark">
      <span class="wordmark__main">Brevel</span>
      <span class="wordmark__sub">Coatings</span>
    </p>
    <p class="slogan">making change simple</p>
    <p class="website">www.Brevel-coatings.com</p>
  </section>

  <section class="card card--back" aria-label="Card back">
    <svg class="card__swoosh" viewBox="0 0 506 298" preserveAspectRatio="none" aria-hidden="true">
      <path d="M0,298 L0,183 C150,222 300,215 390,185 C455,160 492,90 504,0 L506,0 L506,298 Z" fill="var(--leaf)"/>
      <path d="M0,183 C150,222 300,215 390,185 C455,160 492,90 504,0" fill="none" stroke="var(--forest)" stroke-width="2"/>
      <path d="M226,228 C300,222 370,206 420,184 C372,214 300,226 226,228 Z" fill="var(--card)"/>
      <path d="M428,184 C470,152 494,92 502,18 C499,96 474,152 428,184 Z" fill="var(--card)"/>
    </svg>

    <p class="wordmark">
      <span class="wordmark__main">Brevel</span>
      <span class="wordmark__sub">Coatings</span>
    </p>

    <ul class="contact">
      <li class="contact__item">
        <svg class="contact__icon" viewBox="0 0 16 14" aria-hidden="true">
          <path d="M1,4 C1,1 15,1 15,4 L15,5 L11,5 L11,3.5 L5,3.5 L5,5 L1,5 Z" fill="var(--forest)"/>
          <path d="M3,7 L13,7 L14,13 L2,13 Z" fill="var(--forest)"/>
          <circle cx="8" cy="10" r="1.6" fill="var(--leaf)"/>
        </svg>
        <span>(555) 416-9073</span>
      </li>
      <li class="contact__item">
        <span class="contact__icon" aria-hidden="true">@</span>
        <span>d.vask@brevel-coatings.com</span>
      </li>
    </ul>

    <p class="person">Doran Vask</p>
  </section>

</main>
</body>
</html>
```